Brindle Institute Sydney Counsellor iPhone app design

Live wireframes are here;

https://view.frameloft-demo.com/8a2c41d7e09b3f56c1a47d280e9b5c3f61d2a07b#/pages/42918806

Password - brindlesyd482!

We're nearing completion of the Blueprinting phase for our app development project for Brindle Institute Sydney. We need a designs matching the attached functional specification we've created for the app.

VISION
The Sydney Brindle Institute Counselling Services app provides simple and accessible information and engagement with mobile relevant services.
Opening the app, users are greeted with a simple “Hello, how are you today?” a 3 multiple choice answers to both aid in contextual content presentation/navigation specific to the users needs.
Users can access a range of existing web resources from the current website via live in app content and web links. Users can also access a personal folder storing PDF’s that are shared as part of meetings with Brindle Institute Counsellors.
The app also features evolving content pulling from the existing WIKI and presents new and user relevant updates upon opening the app.
Finally, the solution will also deliver support to senior counsellors on each campus by streamlining tasks (such as booking appointments etc). The solution will also provide counsellors with notifications on students at risk and who may need greater support on their journeys.

Target Market(s)

People aged 15 to 24 years
• Students in this age group represent the largest market for
the industry, accounting for an estimated 44.7% of industry revenue in 2014-15. Demand for vocational education from school leavers has declined, as government reforms in higher education have led to more available university places for undergraduate students. Consequently, this market has declined in its share of revenue over the past five years.

People aged 25 to 44 years
• People aged 25 to 44 years are estimated to account for
37.2% of industry revenue. This market has grown its share of revenue over the past five years, as many Australians are entering the system to retrain or update workforce skills due to structural changes occurring in the economy. Students in this age group typically work full- time and therefore undertake their studies part-time, either on-campus or through distance learning.

People aged 45 years and over
• Individuals in this market represent 18.1% of the industry.
The majority of students in this age group have well- established careers, so students undertaking vocational courses are either seeking to upskill or have decided to change careers. As many of these students are employed full-time and often have family commitments, they require more flexible class schedules. This market has remained relatively stable as a share of revenue over the past five years.

Industry/Entity Type

Counsellor

Font styles to use
Sans Serif

Requirements
Must have
• The app needs to meet accessibility guidelines, so no text in images, nice flat design etc.
• The wireframes attached are not to spec, they're just a guide.
• Designs must meet the Apple interface guidelines and device specs for iPhone 4s, 5, 5s, 6 6+
• We also need an app store logo.
Nice to have
• NA

```html
<!DOCTYPE html>
<html lang="en">
<head>
<meta charset="utf-8">
<title>Brindle Institute Counselling App Screens</title>
<link rel="stylesheet" href="https://fonts.googleapis.com/css2?family=Montserrat:wght@400;600&family=Open+Sans:wght@400;600&display=swap">
<style>
  :root {
    --stage: #5e6072;
    --brand: #e9506f;
    --white: #ffffff;
    --ink: #3c3c44;
    --muted: #8a8a93;
    --rule: #e3e3e8;
    --photo-warm: #b08a6a;
    --photo-cool: #6f5a4e;
  }
  * { box-sizing: border-box; margin: 0; padding: 0; }
  html, body { width: 1200px; height: 790px; overflow: hidden; }
  body {
    background: var(--stage);
    font-family: "Open Sans", Arial, sans-serif;
    color: var(--ink);
    display: flex;
    align-items: center;
    justify-content: center;
    gap: 60px;
  }
  .screen {
    width: 330px;
    height: 587px;
    background: var(--white);
    position: relative;
    overflow: hidden;
    display: flex;
    flex-direction: column;
    box-shadow: 0 18px 40px rgba(0,0,0,0.25);
  }
  .status-bar {
    height: 20px;
    display: flex;
    align-items: center;
    justify-content: space-between;
    padding: 0 6px;
    font-size: 9px;
    font-weight: 600;
    color: var(--white);
    background: var(--brand);
  }
  .nav-bar {
    height: 40px;
    background: var(--brand);
    color: var(--white);
    font-family: "Montserrat", Arial, sans-serif;
    font-size: 15px;
    display: flex;
    align-items: center;
    justify-content: center;
    position: relative;
  }
  .nav-menu { position: absolute; left: 12px; top: 13px; }

  /* Splash */
  .splash { background: var(--brand); color: var(--white); }
  .splash .status-bar { background: transparent; }
  .splash-brand {
    margin: 130px 0 0 36px;
    display: flex;
    align-items: center;
    gap: 10px;
    font-family: "Montserrat", Arial, sans-serif;
    font-weight: 600;
    font-size: 22px;
    line-height: 1.1;
  }
  .splash-brand .mark { width: 16px; height: 16px; border-radius: 50%; background: var(--white); flex: none; }
  .splash-greeting {
    position: absolute;
    right: 24px;
    bottom: 34px;
    font-family: "Montserrat", Arial, sans-serif;
    font-size: 15px;
  }

  /* Introduction */
  .hero-photo {
    height: 215px;
    background: linear-gradient(150deg, var(--photo-warm), var(--photo-cool));
  }
  .pager { display: flex; justify-content: center; gap: 6px; margin: 10px 0 8px; }
  .pager span { width: 6px; height: 6px; border-radius: 50%; background: var(--rule); }
  .pager span.active { background: var(--brand); }
  .intro-body { padding: 0 18px; }
  .intro-title {
    font-family: "Montserrat", Arial, sans-serif;
    font-size: 16px;
    font-weight: 600;
    margin-bottom: 8px;
  }
  .intro-text { font-size: 10.5px; line-height: 1.55; color: var(--muted); }
  .button-outline {
    display: block;
    margin: 14px 0 0 auto;
    width: 92px;
    padding: 5px 0;
    border: 1px solid var(--muted);
    border-radius: 14px;
    text-align: center;
    font-size: 11px;
    color: var(--muted);
  }

  /* Welcome */
  .welcome-heading {
    text-align: center;
    margin-top: 20px;
    padding: 0 22px;
    font-family: "Montserrat", Arial, sans-serif;
  }
  .welcome-heading h1 { font-size: 14px; font-weight: 600; line-height: 1.3; }
  .welcome-heading p { font-size: 14px; color: var(--muted); margin-top: 4px; }
  .option { display: flex; flex-direction: column; align-items: center; margin-top: 20px; }
  .option-circle {
    width: 96px; height: 96px; border-radius: 50%;
    display: flex; align-items: center; justify-content: center;
  }
  .option-circle.filled { background: var(--brand); }
  .option-circle.outline { border: 2px solid var(--muted); }
  .option-label { margin-top: 10px; font-size: 13px; font-weight: 600; }
  .divider { height: 1px; background: var(--rule); margin: 18px 0 0; }
</style>
</head>
<body>

  <section class="screen splash" aria-label="Splash screen">
    <div class="status-bar"><span>●●●●○ Wattle Mobile</span><span>4:21 PM</span><span>100%</span></div>
    <div class="splash-brand"><span class="mark"></span><span>Brindle Institute</span></div>
    <p class="splash-greeting">How are you today?</p>
  </section>

  <section class="screen intro" aria-label="Introduction screen">
    <div class="status-bar"><span>●●●●○ Wattle Mobile</span><span>4:21 PM</span><span>100%</span></div>
    <header class="nav-bar">Introduction</header>
    <div class="hero-photo" role="img" aria-label="Photo of a bicycle parked at a rack beside a building"></div>
    <div class="pager"><span class="active"></span><span></span><span></span><span></span><span></span></div>
    <div class="intro-body">
      <h2 class="intro-title">Who Are We?</h2>
      <p class="intro-text">Lorem Ipsum is simply dummy text of the printing and typesetting industry. Lorem Ipsum has been the industry's standard dummy text ever since the 1500s, when an unknown printer took a galley of type and scrambled it to make a type specimen book. It has survived not only five centuries.</p>
      <span class="button-outline">Next Step</span>
    </div>
  </section>

  <section class="screen welcome" aria-label="Welcome screen">
    <div class="status-bar"><span>●●●●○ Wattle Mobile</span><span>4:21 PM</span><span>100%</span></div>
    <header class="nav-bar">
      <svg class="nav-menu" width="16" height="13" viewBox="0 0 16 13" aria-hidden="true">
        <rect y="0" width="16" height="2" fill="#fff"/><rect y="5.5" width="16" height="2" fill="#fff"/><rect y="11" width="16" height="2" fill="#fff"/>
      </svg>
      Welcome
    </header>
    <div class="welcome-heading">
      <h1>Welcome to Brindle Institute Counselling?</h1>
      <p>How can we help you?</p>
    </div>
    <div class="option">
      <div class="option-circle filled">
        <svg width="46" height="46" viewBox="0 0 46 46" aria-hidden="true">
          <circle cx="23" cy="15" r="9" fill="#fff"/>
          <path d="M6 44 C6 31 14 27 23 27 C32 27 40 31 40 44 Z" fill="#fff"/>
        </svg>
      </div>
      <span class="option-label">Talk to someone?</span>
    </div>
    <div class="divider"></div>
    <div class="option">
      <div class="option-circle outline">
        <svg width="48" height="40" viewBox="0 0 48 40" aria-hidden="true">
          <rect x="4" y="4" width="40" height="32" fill="none" stroke="#5a5a63" stroke-width="2.5"/>
          <rect x="10" y="10" width="13" height="12" fill="#5a5a63"/>
          <rect x="26" y="11" width="12" height="2.5" fill="#5a5a63"/>
          <rect x="26" y="17" width="12" height="2.5" fill="#5a5a63"/>
          <rect x="10" y="26" width="28" height="2.5" fill="#5a5a63"/>
        </svg>
      </div>
      <span class="option-label">Articles?</span>
    </div>
  </section>

</body>
</html>
```